CD front and back cover and CD disk. Front includes design elements of the attached band photo, the name of the band (Quiet Harbor Lanterns) and the album name (Paper Anchors?). I've attached a photshoped band photo and an original image. I like the color palette of the photoshoped pix but it may be too dark. So I've attached the original pix, that could be photoshoped. Music is alternative rock. See website qhlTunes.com and the EPK on the site. Songs are not up for this CD yet. Concept - modern, clean, NO gothic rock font or style of any kind.

Back cover needs songs, website and contact as follows:

Hold Ember (Electric)
Linger
Bent and Broken
Meridian
You Sink You Swim
Lean Past You
Hold Ember (Acoustic)
Room To Roam
The Tide
Push Too Far

qhlTunes.com
info@qhlTunes.com
- the actual cd needs the same as above
- use the DiscNook template Sleeve S240 

• Back cover needs the song titles, website, contact info and copyright as follows:
Hold Ember (electric)
Linger
Bent and Broken
Meridian
You Sink You Swim
Lean Past You
Hold Ember (acoustic)
Room To Roam
The Tide
Push Too Far

qhlTune.com
info@qhlTunes.com
Copyright © 2013 Quiet Harbor Lanterns | All Rights Reserved
Also - dimensions for CD Sleeve S240 on discnook.com
Also - CD disk to contain all of the above

```html
<!DOCTYPE html>
<html lang="en">
<head>
<meta charset="utf-8">
<title>Quiet Harbor Lanterns – Paper Anchors? – Sleeve Back</title>
<link rel="stylesheet" href="https://fonts.googleapis.com/css2?family=Carlito:wght@400&family=Cinzel:wght@700&family=Stint+Ultra+Condensed&display=swap">
<style>
  :root {
    --page-bg: #ffffff;
    --mint: #9dd5b3;
    --mint-light: #b9e3c9;
    --mint-deep: #8acca5;
    --ink: #111111;
  }
  * { margin: 0; padding: 0; box-sizing: border-box; }
  html, body {
    width: 1200px;
    height: 900px;
    overflow: hidden;
    background: var(--page-bg);
  }
  .sleeve-back {
    position: absolute;
    left: 211px;
    top: 61px;
    width: 778px;
    height: 778px;
    overflow: hidden;
  }
  .smoke-backdrop {
    position: absolute;
    inset: 0;
    background:
      radial-gradient(ellipse at 30% 25%, var(--mint-light) 0%, transparent 55%),
      radial-gradient(ellipse at 80% 70%, var(--mint-light) 0%, transparent 50%),
      linear-gradient(160deg, var(--mint) 0%, var(--mint-deep) 100%);
  }
  .arc-text {
    position: absolute;
    left: -211px;
    top: -61px;
    width: 1200px;
    height: 900px;
  }
  .band-name {
    font-family: "Cinzel", "Times New Roman", serif;
    font-weight: 700;
    font-size: 46px;
    letter-spacing: 2px;
    fill: var(--ink);
  }
  .copyright {
    font-family: "Carlito", "Calibri", sans-serif;
    font-size: 22px;
    fill: var(--ink);
  }
  .contact {
    position: absolute;
    left: 0;
    top: 348px;
    width: 266px;
    text-align: center;
    font-family: "Carlito", "Calibri", sans-serif;
    font-size: 25px;
    line-height: 31px;
    color: var(--ink);
  }
  .tracklist {
    position: absolute;
    left: 0;
    top: 237px;
    list-style: none;
    font-family: "Carlito", "Calibri", sans-serif;
    font-size: 21px;
    line-height: 27.3px;
    color: var(--ink);
  }
  .tracklist li {
    padding-left: var(--indent);
    white-space: nowrap;
  }
  .album-title {
    position: absolute;
    left: 0;
    width: 778px;
    top: 560px;
    text-align: center;
    font-family: "Stint Ultra Condensed", "Arial Narrow", serif;
    font-size: 56px;
    line-height: 60px;
    color: var(--ink);
  }
</style>
</head>
<body>
  <main class="sleeve-back">
    <div class="smoke-backdrop" role="img" aria-label="Soft drifting smoke wisps over a mint green background"></div>

    <svg class="arc-text" viewBox="0 0 1200 900" aria-hidden="false">
      <defs>
        <path id="upper-arc" d="M 268 460 A 332 332 0 0 1 932 460"/>
        <path id="lower-arc" d="M 253 450 A 347 347 0 0 0 947 450"/>
      </defs>
      <text class="band-name">
        <textPath href="#upper-arc" startOffset="50%" text-anchor="middle">QUIET HARBOR LANTERNS</textPath>
      </text>
      <text class="copyright">
        <textPath href="#lower-arc" startOffset="50%" text-anchor="middle">Copyright © 2013 Quiet Harbor Lanterns | All Rights Reserved</textPath>
      </text>
    </svg>

    <address class="contact">
      qhlTunes.com<br>
      info@qhlTunes.com
    </address>

    <ol class="tracklist">
      <li style="--indent:464px">1. Hold Ember (Electric)</li>
      <li style="--indent:497px">2. Linger</li>
      <li style="--indent:518px">3. Bent And Broken</li>
      <li style="--indent:530px">4. Meridian</li>
      <li style="--indent:537px">5. You Sink You Swim</li>
      <li style="--indent:539px">6. Lean Past You</li>
      <li style="--indent:539px">7. Hold Ember (Acoustic)</li>
      <li style="--indent:533px">8. Room To Roam</li>
      <li style="--indent:521px">9. The Tide</li>
      <li style="--indent:503px">10. Push Too Far</li>
    </ol>

    <h1 class="album-title">Paper Anchors?</h1>
  </main>
</body>
</html>
```